Design some Business Card for shipping company

We need a creative business card designed for a shipping company. All relevant information such as address and phone number can be found on our website. Will need a design for both front and back. The front will container our logo, slogan, contact information etc. The back will have a coupon and some text. check out www.talvorfreight.example for all the information. We need something memorable and unique that will stand out. It needs to a horizontal design. Not vertical.

```html
<!DOCTYPE html>
<html lang="en">
<head>
<meta charset="utf-8">
<title>Talvor Freight – Business Card</title>
<link href="https://fonts.googleapis.com/css2?family=Open+Sans:ital,wght@0,400;0,600;0,700;1,400&display=swap" rel="stylesheet">
<style>
  :root {
    --bg: #cfd0d1;
    --card: #ffffff;
    --green: #1e8a3c;
    --red: #d3252b;
    --black: #1a1a1a;
    --grey: #555555;
  }
  html, body { margin: 0; padding: 0; overflow: hidden; }
  body {
    width: 1200px; height: 1053px;
    background: var(--bg);
    font-family: "Open Sans", Arial, sans-serif;
    display: flex; align-items: center; justify-content: center; gap: 40px;
  }
  .card {
    position: relative;
    width: 540px; height: 309px;
    background: var(--card);
    box-shadow: 0 6px 18px rgba(0,0,0,.18);
    overflow: hidden;
  }
  .flag-bands { position: absolute; right: 0; top: 0; width: 200px; height: 309px; }

  /* front */
  .front .brand-mark {
    position: absolute; left: 70px; top: 70px;
    width: 110px; height: 110px; border-radius: 50%;
    background: #eef1ee;
  }
  .front .brand {
    position: absolute; left: 70px; top: 196px;
  }
  .brand-name {
    margin: 0; color: var(--green); font-weight: 700;
    font-variant: small-caps; letter-spacing: .5px;
  }
  .front .brand-name { font-size: 34px; line-height: 1; }
  .front .slogan { margin: 6px 0 0; font-weight: 700; font-size: 15px; color: var(--black); }
  .front .web { margin: 4px 0 0; font-size: 11px; color: var(--grey); }

  /* back */
  .back .contact { position: absolute; left: 210px; top: 30px; font-size: 11px; line-height: 1.45; color: var(--grey); }
  .back .contact h3 { margin: 0; font-size: 11px; font-weight: 700; color: var(--red); text-transform: uppercase; }
  .back .contact h3 + p { margin: 0 0 4px; }
  .back .contact p { margin: 0; }
  .back .rule { width: 170px; height: 2px; background: var(--green); margin: 2px 0 4px; }
  .back .brand { position: absolute; left: 28px; top: 40px; display: flex; align-items: center; gap: 8px; }
  .back .brand-mark { width: 30px; height: 30px; border-radius: 50%; background: #eef1ee; }
  .back .brand-name { font-size: 17px; }
  .back .about {
    position: absolute; left: 28px; right: 140px; bottom: 28px; margin: 0;
    font-size: 12.5px; line-height: 1.45; font-style: italic; color: var(--green);
  }
</style>
</head>
<body>

  <section class="card back">
    <div class="brand">
      <span class="brand-mark"></span>
      <p class="brand-name">Talvor Freight</p>
    </div>
    <div class="contact">
      <h3>Contact Us</h3>
      <p>USA Tel: +1 555 014 2290<br>KENYA: +254 700 000 118, 0700 000 118</p>
      <div class="rule"></div>
      <h3>Our Shipping Address</h3>
      <p>418 Harbor Loop NE<br>Suite 12<br>Lakemont WA 98000</p>
    </div>
    <p class="about">We provide fast secure ocean shipping service to Kenya from Seattle, Washington. Our rates include customs and duties all the way to Nairobi. All prices are based on volume. Weight does not matter. Delivery is available beyond Nairobi to Eldoret, Kisumu, Nakuru, Webuye, Kitale, Mombasa and Malindi.</p>
    <svg class="flag-bands" viewBox="0 0 200 309" aria-hidden="true">
      <polygon points="60,309 78,309 200,40 200,0" fill="var(--green)"/>
      <polygon points="84,309 100,309 200,90 200,56" fill="var(--red)"/>
      <polygon points="106,309 120,309 200,134 200,104" fill="var(--black)"/>
    </svg>
  </section>

  <section class="card front">
    <span class="brand-mark"></span>
    <div class="brand">
      <p class="brand-name">Talvor Freight</p>
      <p class="slogan">Secure Affordable Shipping to Kenya</p>
      <p class="web">www.talvorfreight.example</p>
    </div>
    <svg class="flag-bands" viewBox="0 0 200 309" aria-hidden="true">
      <polygon points="60,309 78,309 200,40 200,0" fill="var(--green)"/>
      <polygon points="84,309 100,309 200,90 200,56" fill="var(--red)"/>
      <polygon points="106,309 120,309 200,134 200,104" fill="var(--black)"/>
    </svg>
  </section>

</body>
</html>
```